***Retail Packaging Card Design VERY SIMPLE FAST MONEY

Hey guys and gals...

I own a company that makes embroidered patches. We are getting ready to package our item for display in stores. To do so, we have these cool poly bags that seal at the bottom and then have a built-in hole at the top. All you need to do is insert the pre-printed cardstock card and the patch, and it is ready to hang on a wire retail rack.

We have two size bags, and the cards that fit in each will be:
4.25 inches wide x 5.5 inches tall
and
3.25 inches wide x 5.25 inches tall.

Once you have the patch inside, with the card, you are really only working with an available 1.5-inch section above that patch that shows. See examples below.

What I need: some designs for this card that will work with the various types of patches we make. I am willing to pick more than one winner and more than one design if more than one of these works out. I have five themes in mind, and if they are good enough, I am willing to buy all five separately.

First of all, the wording in the design is simply: IRON-ON PATCH.

From there, we want versions of this design that would look right on the following types of patches:

1) American Flag/Patriotic - this would be for a flag you might buy in a military surplus store or in a souvenir store in a city.

2) Rock and Roll - something that might work in a Marlowe's Novelties type of setting - imagine a biohazard patch or a skull and crossbones in the packaging.

3) Scuba Diving. We actually sell a ton of Scuba-related/Diver Down patches and need something specific to those types of stores.

4) Irish patches. Something with a Celtic and/or Ireland design would be great.

5) Generic International Flags. Instead of just one country flag, something that could easily be pictured housing the flag of any country. Some of our stores carry 50-60 styles here, so something that might work with all of them.

One of my main objectives with this product is that the logo/design be EASY TO READ. Imagine walking through a Marlowe's Novelties, a head shop, or an airport gift shop. These will be hanging on a wire rack, and that IRON-ON PATCH must be really easy to read. (That's why we're not doing Embroidered Patch for the text - the word Embroidered is just too hard to read from 5-8 feet and/or looks to squished in). Therefore, I would think the wording would take up a majority of the limited space.

The only other design tip I have is to avoid a white background. One of the sample I will upload has a white background, but a pattern or even just the plain black looks better with a patch inside.

Below I am attaching a few photo links - a couple of really generic mock-ups we did ourselves (they are serviceable but lack any real character, style, or look like they "fit" one of the categories above). I'm also attaching a photo of something similar that a competitor does, just so you can see a patch inside packaging an get a sense of what the final product might look like.

Some very generic mock-ups we've been working with:
http://brindlewoodgoods.example/misc/hangers3.jpg

What these look like with the patches in them:
http://brindlewoodgoods.example/misc/sample1.jpg
http://brindlewoodgoods.example/misc/sample2.jpg

A sample of a competitor's product inside bag with card similar to what you might design:

http://brindlewoodgoods.example/misc/USFLAG.jpg

If you have any questions, or if I have left anything out, please ask and I will post your answer here.

December 18 UPDATE TO DESIGNERS: We have some really good entries in for the "rock" and "patriotic" categories. If you want to submit on these, we encourage more designs, but bring your best. As for Irish, Scuba, and some sort of "works with any flag" category are still somewhat open (especially the first two). Would like to see something on the irish that incorporates either a clover (we sell one at keepsakestitch dot example that would be a good shape/style to use) or the Irish flag or Irish harp. As for the scuba, something red-themed possibly with the red Diver Down flag would be nice.

Requirements
Must have
• Easy to read
Should not have
• Anything too busy to affect readability. Especially any font that is too fancy. Size it to actual size on your screen, stand up and step back 5-8 feet. Is it a blur? Change it.

```html
<!DOCTYPE html>
<html lang="en">
<head>
<meta charset="utf-8">
<title>Iron-On Patch – International Flags Card</title>
<link href="https://fonts.googleapis.com/css2?family=Alfa+Slab+One&family=Bowlby+One&display=swap" rel="stylesheet">
<style>
  :root {
    --card-bg: #ffffff;
    --ink: #111111;
    --outline: #0b0b0b;
    --shadow: rgba(0, 0, 0, 0.45);
    --rule: #1c1f3a;
    --patch-black: #121218;
    --patch-yellow: #f2c62a;
    --patch-red: #d4102a;
    --flag-red: #d52b3a;
    --flag-blue: #2a4a9e;
    --flag-white: #f4f4f4;
    --flag-green: #2f9a3f;
    --flag-yellow: #f0c419;
    --flag-sky: #7fc4ea;
    --flag-orange: #f59a2c;
  }
  html, body {
    margin: 0;
    padding: 0;
    overflow: hidden;
    background: var(--card-bg);
  }
  .card {
    position: relative;
    width: 925px;
    height: 1200px;
    overflow: hidden;
    background: var(--card-bg);
  }
  .flag-row {
    position: absolute;
    border-radius: 10px;
    box-shadow: 0 4px 8px rgba(0,0,0,0.25);
  }
  .flag-row--top {
    left: 14px; top: 18px; width: 880px; height: 62px;
    background: linear-gradient(90deg,
      var(--flag-red) 0%, var(--flag-blue) 8%, var(--flag-white) 13%, var(--flag-red) 18%,
      var(--ink) 27%, var(--flag-yellow) 32%, var(--flag-blue) 38%, var(--flag-white) 47%,
      var(--flag-blue) 54%, var(--flag-red) 58%, var(--flag-green) 64%, var(--flag-green) 72%,
      var(--flag-yellow) 76%, var(--flag-red) 82%, var(--flag-blue) 88%, var(--flag-white) 94%, var(--flag-blue) 100%);
  }
  .flag-row--left {
    left: 20px; top: 240px; width: 292px; height: 84px;
    background: linear-gradient(90deg,
      var(--flag-white) 0%, var(--flag-red) 14%, var(--flag-blue) 30%, var(--flag-white) 45%,
      var(--flag-red) 58%, var(--flag-blue) 70%, var(--flag-sky) 82%, var(--flag-white) 91%, var(--flag-sky) 100%);
  }
  .flag-row--right {
    left: 536px; top: 236px; width: 370px; height: 88px;
    background: linear-gradient(90deg,
      var(--flag-white) 0%, var(--flag-red) 12%, var(--flag-blue) 28%, var(--flag-white) 36%,
      var(--flag-red) 46%, var(--flag-green) 54%, var(--flag-orange) 64%, var(--flag-white) 72%,
      var(--flag-green) 80%, var(--flag-red) 88%, var(--flag-white) 94%, var(--flag-red) 100%);
    transform: skewY(-2deg);
  }
  .title-iron-on {
    position: absolute;
    left: 20px; top: 108px;
    margin: 0;
    z-index: 2;
    font-family: "Bowlby One", "Arial Black", sans-serif;
    font-size: 84px;
    font-weight: 400;
    line-height: 1;
    letter-spacing: 2px;
    color: var(--card-bg);
    -webkit-text-stroke: 4px var(--outline);
    paint-order: stroke fill;
    text-shadow: 6px 10px 10px var(--shadow);
    white-space: nowrap;
  }
  .title-patch {
    position: absolute;
    left: 308px; bottom: 862px;
    margin: 0;
    z-index: 3;
    display: flex;
    align-items: baseline;
    gap: 14px;
    font-family: "Alfa Slab One", "Rockwell", serif;
    font-weight: 400;
    color: var(--ink);
    line-height: 1;
    transform: rotate(-13deg);
    transform-origin: left bottom;
    text-shadow: 6px 10px 12px var(--shadow);
    white-space: nowrap;
  }
  .title-patch span:nth-child(1) { font-size: 100px; }
  .title-patch span:nth-child(2) { font-size: 112px; }
  .title-patch span:nth-child(3) { font-size: 124px; }
  .title-patch span:nth-child(4) { font-size: 137px; }
  .title-patch span:nth-child(5) { font-size: 150px; }
  .patch {
    position: absolute;
    left: 237px; top: 391px;
    width: 500px; height: 752px;
    transform: rotate(-10deg);
    background: linear-gradient(180deg,
      var(--patch-black) 0%, var(--patch-black) 32%,
      var(--patch-yellow) 34%, var(--patch-yellow) 65%,
      var(--patch-red) 67%, var(--patch-red) 100%);
    box-shadow: 2px 4px 6px rgba(0,0,0,0.2);
  }
  .bottom-rule {
    position: absolute;
    left: 0; bottom: 0;
    width: 925px; height: 6px;
    background: var(--rule);
  }
</style>
</head>
<body>
  <main class="card">
    <div class="flag-row flag-row--top" role="img" aria-label="Row of waving international flags"></div>
    <div class="flag-row flag-row--left" role="img" aria-label="Waving flags of several countries"></div>
    <div class="flag-row flag-row--right" role="img" aria-label="Waving flags of several countries"></div>
    <h1 class="title-iron-on">IRON-ON</h1>
    <h2 class="title-patch" aria-label="Patch"><span>P</span><span>A</span><span>T</span><span>C</span><span>H</span></h2>
    <div class="patch" role="img" aria-label="Embroidered tricolour flag patch in black, yellow and red"></div>
    <div class="bottom-rule"></div>
  </main>
</body>
</html>
```